We have a company that provide sandblasted stone products. Example: numbers for houses. Also we sell cultured stone,brick natural stone to the contractor,homeowner. We need to get a business card that describe our product and service. In the original idea we had an old fashion chisel striking through the x in quelvadine.
Updates

Reason: We realized that 2 days was not enough time for the competion to be open many of the designers may be to busy and require more time to compete.

Industry/Entity Type

It Company

Logo Text

Quelvadine

```html
<!DOCTYPE html>
<html lang="en">
<head>
<meta charset="utf-8">
<title>Quelvadine business card</title>
<link rel="stylesheet" href="https://fonts.googleapis.com/css2?family=Inter:wght@300;400;600&display=swap">
<style>
  :root {
    --canvas: #dcdcdc;
    --card-brand: #f7f7f7;
    --card-contact: #e9e9e9;
    --ink: #1d1d1d;
    --ink-soft: #2a2a2a;
    --accent: #e8501e;
  }
  * { margin: 0; padding: 0; box-sizing: border-box; }
  html, body {
    width: 1200px;
    height: 1000px;
    overflow: hidden;
    background: var(--canvas);
  }
  .canvas {
    width: 1200px;
    height: 1000px;
    display: flex;
    align-items: center;
    justify-content: center;
    gap: 40px;
  }
  .card {
    position: relative;
    width: 540px;
    height: 309px;
    overflow: hidden;
    box-shadow: 0 6px 18px rgba(0, 0, 0, 0.18);
    font-family: "Inter", Arial, sans-serif;
  }

  /* contact side */
  .card--contact {
    background: var(--card-contact);
    color: var(--ink);
  }
  .contact {
    position: absolute;
    left: 40px;
    top: 56px;
    right: 40px;
  }
  .contact__name {
    font-size: 27px;
    font-weight: 600;
    letter-spacing: 0.2px;
    margin-left: 150px;
    margin-bottom: 22px;
  }
  .contact__line {
    font-size: 21px;
    font-weight: 400;
    line-height: 1.25;
    color: var(--ink-soft);
  }

  /* brand side */
  .card--brand {
    background: var(--card-brand);
    display: flex;
    align-items: center;
    justify-content: center;
    gap: 22px;
  }
  .brand__name {
    font-weight: 300;
    font-size: 30px;
    letter-spacing: 13px;
    color: var(--ink);
  }
  .brand__dot {
    width: 18px;
    height: 18px;
    border-radius: 50%;
    background: var(--accent);
  }
</style>
</head>
<body>
  <main class="canvas">
    <section class="card card--contact" aria-label="Contact side">
      <div class="contact">
        <p class="contact__name">Rowan Kestrel</p>
        <p class="contact__line">T: (917) 555-0148</p>
        <p class="contact__line">rowan@quelvadine.com</p>
      </div>
    </section>

    <section class="card card--brand" aria-label="Brand side">
      <span class="brand__name">QUELVADINE</span>
      <span class="brand__dot" aria-hidden="true"></span>
    </section>
  </main>
</body>
</html>
```